Wattlegrove Aged Care Centre

We need a website design for an aged care facility in Brisbane (a different one to project already posted) with final design provided as a .psd file.

This website will be built on Dot Net Nuke so design needs to be able to be converted into a DNN skin and containers.

Target Market(s)

• Credibility
• Family orientated
• Establish an online identity
• Download a booking form for tours
• Receive general enquiries
• Feature a phone number
• Advertise career opportunities

Number of Pages Required

1 page

Requirements
Must have
• o The following elements are to be included in the design concepts:
• o Phone number will be featured in banner 07 3821 4476
• o Logo and words Marstow Care Centre to be featured in banner
• o Area for a flash banner of rotating images on homepage (have attached some images)
• o 3 x buttons to be designed and feature on homepage - Book a Tour, Contact Us and Sign up to our newsletter
• o No colour preference but perhaps keeping with their logo/branding but am open to ideas

```html
<!DOCTYPE html>
<html lang="en">
<head>
<meta charset="utf-8">
<title>Marstow Care Centre</title>
<link href="https://fonts.googleapis.com/css2?family=Arimo:wght@400;700&display=swap" rel="stylesheet">
<style>
:root{
  --white:#ffffff;
  --nav:#0f320a;
  --hero:#244a1f;
  --panel-dark:#1f4219;
  --panel-light:#8aa882;
  --main:#66805f;
  --box:#567a4e;
  --heading:#1f4a1a;
  --gold:#f4c018;
  --gold-dark:#e0a800;
  --phone:#5e7e55;
  --brand:#27511f;
  --text-dark:#1c3818;
}
*{margin:0;padding:0;box-sizing:border-box}
html,body{width:1029px;height:1200px;overflow:hidden}
body{position:relative;background:var(--main);font-family:"Arimo",Arial,sans-serif;color:var(--white)}
.abs{position:absolute}

.header{left:0;top:0;width:1029px;height:140px;background:var(--white)}
.brand-mark{left:128px;top:23px;width:86px;height:86px;border-radius:50%;background:var(--brand)}
.brand-name{left:239px;top:60px;font-size:15.5px;color:var(--brand)}
.header-flourish{left:665px;top:0;width:310px;height:100px;background:radial-gradient(ellipse at 50% 30%,#f7e6c0 0%,rgba(255,255,255,0) 70%)}
.phone{right:129px;top:102px;font-size:21px;color:var(--phone)}

.nav{left:0;top:140px;width:1029px;height:26px;background:var(--nav)}
.nav a{position:absolute;top:0;height:26px;line-height:26px;font-size:11px;color:var(--white);text-decoration:none;transform:translateX(-50%)}
.nav a.active{background:var(--white);color:#000;width:91px;text-align:center}

.hero{left:0;top:166px;width:1029px;height:325px;background:var(--hero)}
.hero-photo{left:127px;top:195px;width:583px;height:267px;background:linear-gradient(100deg,#e8e2d8 0%,#cfd4d8 50%,#9cb3c2 75%,#c9b79a 100%)}

.newsletter{left:720px;top:196px;width:180px;height:146px;background:var(--panel-light);border-radius:8px 8px 0 0}
.newsletter h2{position:absolute;left:12px;top:9px;font-weight:400;font-size:14px;color:var(--white)}
.newsletter .rule{position:absolute;left:12px;top:33px;width:157px;height:1px;background:#d6e2d2}
.newsletter label{position:absolute;left:12px;font-size:10px;color:#000}
.newsletter .field{position:absolute;left:56px;width:111px;height:15px;background:var(--white)}
.signup{position:absolute;right:13px;top:109px;width:59px;height:20px;border-radius:5px;background:linear-gradient(#ffffff,#d8d8d8);color:#111;font-size:10px;letter-spacing:.5px;text-align:center;line-height:20px}

.actions{left:720px;top:347px;width:180px;height:116px;background:var(--panel-dark)}
.pill{position:absolute;left:20px;width:141px;height:36px;border:1px solid var(--white);border-radius:18px;font-size:13px;letter-spacing:.5px;line-height:34px;padding-left:50px}
.pill svg{position:absolute;left:14px;top:9px}

.welcome{left:127px;top:505px;width:401px;height:201px;background:var(--box)}
.welcome h1{position:absolute;left:35px;top:20px;font-size:17px;letter-spacing:.8px;color:var(--heading)}
.welcome p{position:absolute;left:36px;top:68px;width:330px;font-size:11.8px;line-height:14.4px;letter-spacing:.2px;color:var(--text-dark)}
.btn{position:absolute;background:var(--gold);border:1px solid #7b5a00;border-radius:5px;color:#4a3000;font-size:12px;letter-spacing:.5px;text-align:center}
.facilities-photo{left:528px;top:505px;width:372px;height:201px;background:linear-gradient(180deg,#e9e4da 0%,#a89a7c 45%,#7e6247 70%,#d6b34a 100%)}

.section-title{top:718px;font-size:17px;font-weight:700;letter-spacing:.8px;color:var(--gold)}
.about{left:127px;top:749px;width:493px;height:343px;background:var(--box)}
.about p{position:absolute;left:14px;width:470px;font-size:10.3px;line-height:12.4px;color:var(--white)}
.gallery{left:631px;top:749px;width:269px;height:343px;background:var(--box)}
.thumb{position:absolute;left:36px;width:196px;height:83px;border:1px solid #e6e6e6;border-radius:3px}

.footer{left:0;top:1113px;width:1029px;height:87px;background:var(--hero);border-top:1px solid #c7a02a}
.footer-links{position:absolute;left:0;width:1029px;top:25px;text-align:center;font-size:9.5px}
.footer-links .current{color:var(--gold)}
.copyright{position:absolute;left:0;width:1029px;top:50px;text-align:center;font-size:7.5px}
</style>
</head>
<body>

<header class="header abs">
  <div class="brand-mark abs"></div>
  <div class="brand-name abs">Marstow Care Centre</div>
  <div class="header-flourish abs" role="img" aria-label="Soft floral flourish in cream tones"></div>
  <div class="phone abs">Call (07) 3821 4476</div>
</header>

<nav class="nav abs">
  <a href="#" style="left:241px">Home</a>
  <a href="#" class="active" style="left:343px">About Us</a>
  <a href="#" style="left:453px">Facilities</a>
  <a href="#" style="left:556px">Tours</a>
  <a href="#" style="left:652px">Careers</a>
  <a href="#" style="left:764px">Contact Us</a>
</nav>

<section class="hero abs"></section>
<div class="hero-photo abs" role="img" aria-label="Rotating banner photo of a smiling resident in a bright lounge"></div>

<form class="newsletter abs">
  <h2>Sign Up for News Letter</h2>
  <div class="rule"></div>
  <label style="top:56px">Name &nbsp;:</label><div class="field" style="top:53px"></div>
  <label style="top:85px">e-mail :</label><div class="field" style="top:82px"></div>
  <div class="signup">SIGN UP</div>
</form>

<div class="actions abs">
  <div class="pill" style="top:15px">
    <svg width="18" height="18" viewBox="0 0 18 18" fill="none" stroke="#fff" stroke-width="1.3"><rect x="2" y="1" width="13" height="16"/><path d="M6 14 L12 4 M9 14 L13 8"/></svg>
    Book a tour
  </div>
  <div class="pill" style="top:65px">
    <svg width="22" height="16" viewBox="0 0 22 16" fill="#fff"><path d="M1 5 Q11 -2 21 5 L19 8 L15 6 L15 4 Q11 2 7 4 L7 6 L3 8 Z"/><path d="M5 9 L8 6 L14 6 L17 9 L17 15 L5 15 Z"/><circle cx="11" cy="11" r="2" fill="#1f4219"/></svg>
    Contact Us
  </div>
</div>

<section class="welcome abs">
  <h1>Welcome to the Marstow Care Centre</h1>
  <p>Lorem ipsum dolor sit amet, consectetur adipiscing elit.Praesent et orci diam. Sed commodo tellus etnunc rutrum nec sollicitudin velit facilisis. Vivamusleo nec quam gravida nec gravida ligula aliquam.Etiam sapien nibh, venenatis ut venenatis id, gravsed quam. Sed id orci orci, faucibus accumsan eni.</p>
  <div class="btn" style="left:313px;top:165px;width:66px;height:23px;line-height:21px">more</div>
</section>
<div class="facilities-photo abs" role="img" aria-label="Photo of the centre's covered entrance with columns and timber doors"></div>
<div class="btn abs" style="left:813px;top:669px;width:76px;height:23px;line-height:21px">Facilities</div>

<h2 class="section-title abs" style="left:147px">Little about&nbsp; Marstow Care Centre</h2>
<h2 class="section-title abs" style="left:641px">Gallery</h2>

<section class="about abs">
  <p style="top:24px">Lorem ipsum dolor sit amet, consectetur adipiscing elit.Praesent et orci diam. Sed commodo tellus etnunc rutrum nec sollicitudin velit facilisis. Vivamusleo nec quam gravida nec gravida ligula aliquam.Etiam sapiennibh, venenatis ut venenatis id, gravsed quam. Sed idorci orci,fa ucibus accumsan eni.</p>
  <p style="top:86px">Lorem ipsum dolor sit amet, consectetur adipiscing elit.Praesent et orci diam. Sed commodo tellus etnunc rutrum nec sollicitudin velit facilisis. Vivamusleo nec quam gravida nec gravida ligula aliquam.Etiam sapiennibh, venenatis ut venenatis id, gravsed quam. Sed idorci orci,fa ucibus accumsan eni.</p>
  <p style="top:148px">Lorem ipsum dolor sit amet, consectetur adipiscing elit.Praesent et orci diam. Sed commodo tellus etnunc rutrum nec sollicitudin velit facilisis. Vivamusleo nec quam gravida nec gravida ligula aliquam.Etiam sapiennibh, venenatis ut venenatis id, gravsed quam. Sed idorci orci,fa ucibus accumsan eni.</p>
  <p style="top:210px">Lorem ipsum dolor sit amet, consectetur adipiscing elit.Praesent et orci diam. Sed commodo tellus etnunc rutrum nec sollicitudin velit facilisis. Vivamusleo nec quam gravida nec gravida ligula aliquam.Etiam sapiennibh, venenatis ut venenatis id, gravsed quam. Sed idorci orci,fa ucibus accumsan eni.</p>
  <p style="top:272px">Lorem ipsum dolor sit amet, consectetur adipiscing elit.Praesent et orci diam. Sed commodo tellus etnunc rutrum nec sollicitudin velit facilisis. Vivamusleo nec quam gravida nec gravida ligula aliquam.Etiam sapiennibh, venenatis ut venenatis id, gravsed quam. Sed idorci orci,fa ucibus accumsan eni.</p>
</section>

<section class="gallery abs">
  <div class="thumb" style="top:26px;background:linear-gradient(160deg,#a8b0b8,#8a7458 50%,#4c5a3a)" role="img" aria-label="Gallery photo of the brick building and garden"></div>
  <div class="thumb" style="top:120px;background:linear-gradient(180deg,#e8e2d4,#7e5a3c 55%,#b8a88c)" role="img" aria-label="Gallery photo of the columned entrance"></div>
  <div class="thumb" style="top:212px;background:linear-gradient(170deg,#cfc8bc,#a27448 55%,#ded8cc)" role="img" aria-label="Gallery photo of the kitchen with timber cabinets"></div>
  <div class="btn" style="left:173px;top:309px;width:83px;height:23px;line-height:21px">see gallery</div>
</section>

<footer class="footer abs">
  <div class="footer-links">| Home | <span class="current">About Us</span> | Facilities | Tours | Careers | Contact Us |</div>
  <div class="copyright">Copyright @ Marstow Care Centre 2009</div>
</footer>

</body>
</html>
```